New Business Card Design Project

Use the flyer uploaded and website www.brightoakbuilders.com for inspiration.
List Our Services on Backside of business cards
Martin Hollis
Harborline Renovations Inc.
Licensed General Contractors
858-471-9063

Contact Information for Business Card

Use the flyer uploaded and website www.brightoakbuilders.com for inspiration. List Our Services on Backside of business cards Martin Hollis Harborline Renovations Inc. Licensed General Contractors 858-471-9063

```html
<!DOCTYPE html>
<html lang="en">
<head>
<meta charset="utf-8">
<title>Harborline Renovations – Business Card</title>
<link href="https://fonts.googleapis.com/css2?family=Cinzel:wght@400&family=PT+Sans:wght@400;700&display=swap" rel="stylesheet">
<style>
  :root {
    --backdrop: #2e2e30;
    --card-dark: #121212;
    --card-light: #ffffff;
    --ink-light: #f2f2f2;
    --ink-dark: #111111;
  }
  * { box-sizing: border-box; margin: 0; padding: 0; }
  html, body { width: 900px; height: 1200px; overflow: hidden; }
  body { background: var(--backdrop); position: relative; font-family: "PT Sans", sans-serif; }

  .card {
    position: absolute; left: 133px; width: 632px; height: 364px;
    box-shadow: 0 6px 18px rgba(0,0,0,.45);
  }
  .card--back { top: 210px; background: var(--card-dark); color: var(--ink-light); }
  .card--front { top: 624px; background: var(--card-light); color: var(--ink-dark); }

  .brand-name {
    position: absolute; left: 40px; width: 300px; top: 138px;
    font-family: "Cinzel", serif; font-weight: 400; font-size: 27px;
    line-height: 1.25; letter-spacing: 1px; text-align: center;
  }

  .services { position: absolute; left: 373px; top: 54px; }
  .services__guarantee { font-weight: 700; font-size: 14px; line-height: 18px; text-transform: uppercase; }
  .services__label {
    display: inline-block; margin-top: 3px; margin-bottom: 7px;
    background: var(--ink-light); color: var(--ink-dark);
    font-weight: 700; font-size: 14px; letter-spacing: .5px; line-height: 18px;
    padding: 0 24px 0 21px;
    clip-path: polygon(0 0, 100% 0, 93% 100%, 0 100%);
  }
  .services__list { list-style: none; }
  .services__item {
    display: flex; align-items: center; gap: 7px;
    font-size: 14px; line-height: 22.4px; letter-spacing: .3px;
  }
  .services__item svg { width: 14px; height: 14px; flex: none; }

  .person { position: absolute; left: 372px; top: 96px; }
  .person__name { font-family: "Cinzel", serif; font-size: 25px; letter-spacing: 1.5px; line-height: 30px; }
  .person__role { font-size: 13.5px; margin-top: 3px; letter-spacing: .2px; }

  .contact { position: absolute; left: 372px; top: 200px; list-style: none; }
  .contact__item {
    display: flex; align-items: center; gap: 6px;
    font-size: 13.5px; line-height: 25.5px; letter-spacing: .8px;
  }
  .contact__item svg { width: 14px; height: 14px; flex: none; }
</style>
</head>
<body>

<section class="card card--back" aria-label="Card back: services">
  <div class="brand-name">Harborline<br>Renovations</div>

  <div class="services">
    <p class="services__guarantee">Our services are<br>100% guaranteed</p>
    <span class="services__label">SPECIALIZING IN:</span>
    <ul class="services__list">
      <li class="services__item"><svg viewBox="0 0 14 14"><rect x="1" y="3" width="10" height="10" fill="none" stroke="currentColor" stroke-width="1.6"/><path d="M3.5 7.5l2.5 2.5L13 2" fill="none" stroke="currentColor" stroke-width="2"/></svg>Remodel: Kitchen &amp; Bath</li>
      <li class="services__item"><svg viewBox="0 0 14 14"><rect x="1" y="3" width="10" height="10" fill="none" stroke="currentColor" stroke-width="1.6"/><path d="M3.5 7.5l2.5 2.5L13 2" fill="none" stroke="currentColor" stroke-width="2"/></svg>Painting: Interior &amp; Exterior</li>
      <li class="services__item"><svg viewBox="0 0 14 14"><rect x="1" y="3" width="10" height="10" fill="none" stroke="currentColor" stroke-width="1.6"/><path d="M3.5 7.5l2.5 2.5L13 2" fill="none" stroke="currentColor" stroke-width="2"/></svg>Flooring: Carpet, Vinyl, Wood</li>
      <li class="services__item"><svg viewBox="0 0 14 14"><rect x="1" y="3" width="10" height="10" fill="none" stroke="currentColor" stroke-width="1.6"/><path d="M3.5 7.5l2.5 2.5L13 2" fill="none" stroke="currentColor" stroke-width="2"/></svg>Window &amp; Door Replacement</li>
      <li class="services__item"><svg viewBox="0 0 14 14"><rect x="1" y="3" width="10" height="10" fill="none" stroke="currentColor" stroke-width="1.6"/><path d="M3.5 7.5l2.5 2.5L13 2" fill="none" stroke="currentColor" stroke-width="2"/></svg>Plumbing: Repairs &amp; Upgrades</li>
      <li class="services__item"><svg viewBox="0 0 14 14"><rect x="1" y="3" width="10" height="10" fill="none" stroke="currentColor" stroke-width="1.6"/><path d="M3.5 7.5l2.5 2.5L13 2" fill="none" stroke="currentColor" stroke-width="2"/></svg>Energy-Efficient Upgrades</li>
      <li class="services__item"><svg viewBox="0 0 14 14"><rect x="1" y="3" width="10" height="10" fill="none" stroke="currentColor" stroke-width="1.6"/><path d="M3.5 7.5l2.5 2.5L13 2" fill="none" stroke="currentColor" stroke-width="2"/></svg>Deck &amp; Patio Construction</li>
      <li class="services__item"><svg viewBox="0 0 14 14"><rect x="1" y="3" width="10" height="10" fill="none" stroke="currentColor" stroke-width="1.6"/><path d="M3.5 7.5l2.5 2.5L13 2" fill="none" stroke="currentColor" stroke-width="2"/></svg>Water &amp; Mold Damage</li>
      <li class="services__item"><svg viewBox="0 0 14 14"><rect x="1" y="3" width="10" height="10" fill="none" stroke="currentColor" stroke-width="1.6"/><path d="M3.5 7.5l2.5 2.5L13 2" fill="none" stroke="currentColor" stroke-width="2"/></svg>Garage Renovation</li>
    </ul>
  </div>
</section>

<section class="card card--front" aria-label="Card front: contact">
  <div class="brand-name">Harborline<br>Renovations</div>

  <div class="person">
    <h1 class="person__name">MARTIN HOLLIS</h1>
    <p class="person__role">Business development manager</p>
  </div>

  <ul class="contact">
    <li class="contact__item"><svg viewBox="0 0 14 14"><path d="M3 1l2.5 2.8-1.4 1.9c.8 1.7 2.1 3 3.8 3.9l1.9-1.4L12.6 10.7 11.2 13C6 12.6 1.4 8 1 2.8z" fill="currentColor"/></svg>858-471-9063</li>
    <li class="contact__item"><svg viewBox="0 0 14 14"><rect x="0.5" y="3" width="13" height="8.5" fill="currentColor"/><path d="M1 3.5l6 4.5 6-4.5" fill="none" stroke="#fff" stroke-width="1.1"/></svg>mh@brightoakbuilders.com</li>
    <li class="contact__item"><svg viewBox="0 0 14 14" fill="none" stroke="currentColor" stroke-width="1.1"><circle cx="7" cy="7" r="6"/><ellipse cx="7" cy="7" rx="2.6" ry="6"/><path d="M1 7h12M2 4h10M2 10h10"/></svg>www.brightoakbuilders.com</li>
  </ul>
</section>

</body>
</html>
```